Fern Ledge Maplecrest Music Festival Poster

We are a summer music festival with concerts spanning Jazz, Cabaret, Education, Broadway, Chamber and Opera. We are looking for our key art for the 2016 season. This design will serve as the basis for all promotional materials, the concert program, and our web materials. Though eventually this means we will need to adjust the design to fit many different sizes, our poster will be printed mostly on 8.5" x 11" paper, and we can adapt from there. The design will be featured online and in print. It should be vertical and not landscape.

WE ARE SEEKING SLEEK, ELEGANT DESIGNS WITH MAYBE A KEY STOCK PHOTOGRAPH AND THE RELEVANT TEXT/DETAILS.

PLEASE NOTE: The included file "avenir logo.psd" is just a suggestion for the feel we are going for. It is our "working logo" after having scraped our old logo. We are interested in seeing your own ideas on how to style the brand name, but if you have ideas working with this version of the logo, feel free to use it.

REQUIRED DETAILS:
Festival Name: Fern Ledge Maplecrest Music Festival
Dates: July 29 - August 7 2016 (the year, 2016, must be included on the poster, but it does not need to be in the same location as where the actual dates are listed)
Website: www.fernledgemaplecrestfest.example

Additional Information:
- the 7 musical styles (jazz, choral, cabaret, education, broadway, chamber, opera) are important to defining who we are. You may decide to include these on the poster.
- We are looking for a very elegant design

TARGET:
We depend highly on an older clientele. We are working to expand our brand into younger demographics, but we want to be sure that we do not alienate our current consumer base with text that may be difficult for them to read.
Updates

Project Deadline Extended Reason: I am extending the deadline because it is taking longer to get feedback from my superiors than I had expected. Extending the deadline will give me time to provide adequate feedback from the people who will ultimately be making the decision. Thank you. Added Saturday, January 30, 2016

Sorry for the delay. There were issues with the decision makers but we are selecting in the next 24 hours.

Target Market(s)

Lovers of the styles of music we feature. We have a good number of elderly consumers, but also families and school groups (discussed further in description section)

Industry/Entity Type

Entertainment

Font styles to use
Sans Serif

Requirements
Must have
• Festival Name: Fern Ledge Maplecrest Music Festival
• Dates: July 29 - August 7 2016 (the year, 2016, must be included on the poster, but it does not need to be in the same location as where the actual dates are listed)
• Website: www.fernledgemaplecrestfest.example
Nice to have
• - the 7 musical styles (jazz, choral, cabaret, education, broadway, chamber, opera) are important to defining who we are. We would love to include these styles somewhere on the image, or feature them somehow in the artwork
• - Our brand has an elegance to it due to the type of music we offer, and our location being in a very natural space. inclusion of the music/nature mixed aspect of our brand in artwork might be nice
Should not have
• Anything that may offend or alienate an older, more conservative demographic

```html
<!DOCTYPE html>
<html lang="en">
<head>
<meta charset="utf-8">
<title>Fern Ledge Maplecrest Music Festival 2016</title>
<link href="https://fonts.googleapis.com/css2?family=Lato:wght@300;400;700;900&display=swap" rel="stylesheet">
<style>
  :root {
    --stage: #1c1c1c;
    --sky-top: #aee0f7;
    --sky-low: #c9ecfb;
    --crimson: #e2315d;
    --badge: #0f4253;
    --badge-ring: #27354a;
    --rule: #5bb8e6;
    --white: #ffffff;
    --sand: #f0cd8c;
    --pine-light: #178b6e;
    --pine-dark: #0b4f3e;
    --wash-pink: #ee5b93;
    --wash-orange: #f2843f;
    --wash-yellow: #f7d96a;
    --wash-red: #e4383f;
  }
  * { margin: 0; padding: 0; box-sizing: border-box; }
  html, body {
    width: 1200px; height: 1200px; overflow: hidden;
    background: var(--stage);
    font-family: "Lato", Arial, sans-serif;
  }
  .poster {
    position: absolute; left: 165px; top: 18px;
    width: 870px; height: 1164px; overflow: hidden;
    background: linear-gradient(180deg, var(--sky-top) 0%, var(--sky-low) 60%, var(--sky-top) 100%);
  }
  .styles {
    position: absolute; top: 44px; left: 0; right: 0;
    text-align: center; color: var(--crimson);
    font-weight: 400; font-size: 36px; line-height: 46px;
    word-spacing: 16px; letter-spacing: -0.5px;
  }
  .landscape {
    position: absolute; left: 0; right: 0; top: 790px; bottom: 0;
    background: linear-gradient(180deg, var(--sand) 0%, var(--sand) 10%, var(--pine-light) 22%, var(--pine-dark) 100%);
  }
  .instrument-wash {
    position: absolute; left: 20px; top: 160px; width: 860px; height: 790px;
    border-radius: 46% 40% 48% 42% / 42% 48% 40% 50%;
    background:
      radial-gradient(circle at 30% 20%, var(--wash-yellow) 0%, transparent 30%),
      radial-gradient(circle at 80% 35%, var(--wash-pink) 0%, transparent 40%),
      radial-gradient(circle at 25% 70%, var(--wash-red) 0%, transparent 38%),
      radial-gradient(circle at 70% 85%, var(--wash-orange) 0%, transparent 35%),
      radial-gradient(circle at 50% 50%, #f08aa8 0%, #f6b1b9 55%, transparent 72%);
    opacity: 0.9;
  }
  .badge {
    position: absolute; left: 205px; top: 300px;
    width: 488px; height: 488px; border-radius: 50%;
    background: var(--badge);
    border: 9px solid var(--badge-ring);
    color: var(--white); text-align: center;
  }
  .badge .name-top {
    margin-top: 82px; font-weight: 900; font-size: 58px; line-height: 58px; letter-spacing: -2px;
  }
  .badge .name-main {
    font-weight: 700; font-size: 76px; line-height: 78px; letter-spacing: -3px;
  }
  .badge .name-sub {
    font-weight: 300; font-size: 54px; line-height: 62px; letter-spacing: -1px;
  }
  .badge .rule {
    width: 390px; height: 3px; margin: 20px auto 0; background: var(--rule);
  }
  .badge .dates {
    margin-top: 22px; font-weight: 400; font-size: 31px; letter-spacing: -0.5px;
  }
  .badge .year {
    margin-top: 16px; font-weight: 700; font-size: 32px; letter-spacing: 5px;
  }
  .website {
    position: absolute; left: 0; right: 0; top: 1084px;
    text-align: center; color: var(--white);
    font-weight: 400; font-size: 25px; letter-spacing: -0.5px;
  }
</style>
</head>
<body>
  <main class="poster">
    <p class="styles">JAZZ CHORAL CABARET EDUCATION<br>BROADWAY CHAMBER OPERA</p>
    <div class="landscape" role="img" aria-label="Sandy mountain ridge behind a dense pine forest"></div>
    <div class="instrument-wash" role="img" aria-label="Watercolour splash of violins, guitars, trumpet and accordion in pink, red, orange and yellow"></div>
    <section class="badge">
      <h1>
        <span class="name-top" style="display:block">FERN LEDGE</span>
        <span class="name-main" style="display:block">Maplecrest</span>
        <span class="name-sub" style="display:block">Music Festival</span>
      </h1>
      <div class="rule"></div>
      <p class="dates">July 29 - August 7</p>
      <p class="year">2016</p>
    </section>
    <p class="website">www.fernledgemaplecrestfest.example</p>
  </main>
</body>
</html>
```